Hvac and insulation company needs good looking business card design

We are hvac and insulation company and looking for a new business cards that look to today standards designs

Target Market(s)

homeowners

Industry/Entity Type

Hvac

Contact Information for Business Card

Name: Dorian Velkova
Home comfort consultant
address: 4827 Marrow Ridge Rd #215 Oakland, CA 94611
office: 888-317-5069
cell: 510-642-1388
Lic.# 458127
Email: dorian@quarry-hvac.com
Web: quarry-hvac.com

Requirements
Must have
• clean and sleek look
Nice to have
• simple with a clean look
Should not have
• to busy business card

```html
<!DOCTYPE html>
<html lang="en">
<head>
<meta charset="utf-8">
<title>Quarry – Business Card</title>
<link href="https://fonts.googleapis.com/css2?family=Open+Sans:wght@400;600;700&display=swap" rel="stylesheet">
<style>
  :root {
    --bg: #b9b9b9;
    --card: #ffffff;
    --orange: #ff6a00;
    --ink: #1a1a1a;
    --muted: #555555;
    --slate: #555555;
  }
  * { margin: 0; padding: 0; box-sizing: border-box; }
  html, body { width: 1200px; height: 1200px; overflow: hidden; }
  body {
    background: var(--bg);
    font-family: "Open Sans", Arial, sans-serif;
    position: relative;
  }
  .card {
    position: absolute;
    left: 216px;
    width: 765px;
    height: 462px;
    overflow: hidden;
    box-shadow: 0 1px 3px rgba(0,0,0,0.15);
  }
  .card-front {
    top: 134px;
    background: var(--card);
    border-radius: 0 48px 0 48px;
  }
  .card-back {
    top: 607px;
    background: var(--orange);
    border-radius: 48px 0 48px 0;
  }
  .front-band { position: absolute; left: 0; top: 0; }
  .brand {
    position: absolute;
    display: flex;
    align-items: center;
    font-weight: 700;
    letter-spacing: -0.01em;
  }
  .brand-dot { border-radius: 50%; flex: none; }
  .card-front .brand { left: 48px; top: 186px; color: var(--orange); font-size: 60px; gap: 14px; }
  .card-front .brand-dot { width: 28px; height: 28px; background: var(--orange); }
  .card-back .brand { left: 0; right: 0; top: 160px; justify-content: center; color: #fff; font-size: 110px; gap: 24px; }
  .card-back .brand-dot { width: 52px; height: 52px; background: #fff; }
  .holder {
    position: absolute;
    right: 55px;
    top: 36px;
    text-align: right;
  }
  .holder-name { font-size: 32px; font-weight: 600; color: var(--ink); line-height: 1.2; }
  .holder-title { font-size: 21px; color: var(--muted); line-height: 1.3; }
  .contact {
    position: absolute;
    left: 402px;
    top: 161px;
    font-size: 18.5px;
    color: var(--ink);
    line-height: 25px;
  }
  .contact-row { display: flex; }
  .contact-row + .contact-row { margin-top: 0; }
  .contact-row.gap { margin-top: 14px; }
  .contact-label { width: 30px; }
  .contact-value { width: 300px; }
  .licence {
    position: absolute;
    left: 0;
    width: 765px;
    padding-left: 280px;
    top: 366px;
    text-align: center;
    font-size: 23px;
    color: var(--ink);
  }
  .back-url {
    position: absolute;
    left: 0;
    right: 0;
    top: 404px;
    text-align: center;
    color: #fff;
    font-size: 22px;
    letter-spacing: 0.62em;
    padding-left: 0.62em;
  }
</style>
</head>
<body>
  <section class="card card-front">
    <svg class="front-band" width="765" height="462" viewBox="0 0 765 462" aria-hidden="true">
      <polygon points="80,410 624,410 516,424" fill="var(--slate)"/>
      <polygon points="0,415 516,430 765,411 765,462 0,462" fill="var(--orange)"/>
    </svg>

    <div class="brand"><span class="brand-dot"></span>quarry</div>

    <div class="holder">
      <h1 class="holder-name">Dorian Velkova</h1>
      <p class="holder-title">Home comfort consultant</p>
    </div>

    <div class="contact">
      <div class="contact-row"><span class="contact-label">A</span><span class="contact-value">: 4827 Marrow Ridge Rd #215 Oakland, CA 94611</span></div>
      <div class="contact-row gap"><span class="contact-label">P</span><span class="contact-value">: 888-317-5069</span></div>
      <div class="contact-row"><span class="contact-label">C</span><span class="contact-value">: 510-642-1388</span></div>
      <div class="contact-row"><span class="contact-label">E</span><span class="contact-value">: dorian@quarry-hvac.com</span></div>
      <div class="contact-row gap"><span class="contact-label">W</span><span class="contact-value">: www.quarry-hvac.com</span></div>
    </div>

    <p class="licence">Lic.# 458127</p>
  </section>

  <section class="card card-back">
    <div class="brand"><span class="brand-dot"></span>quarry</div>
    <p class="back-url">www.quarry-hvac.com</p>
  </section>
</body>
</html>
```